Finally a Vodka produced for women ! (Label Design)

We are a small distillery based in Melbourne, Australia and we need a Vodka label design solution that will appeal to women aged 30-50 years and radiate luxury. Full Details are in a design brief attached. We thank you in advance.

Target Market(s)

Affluent females 30-50 years.

Industry/Entity Type

Spirits/Alcohol

Requirements
Must have
• Be clear this is a luxury Vodka.
Nice to have
• Elegance.

```html
<!DOCTYPE html>
<html lang="en">
<head>
<meta charset="utf-8">
<title>Silver Wren Distillery – Premium Vodka Label</title>
<link rel="stylesheet" href="https://fonts.googleapis.com/css2?family=Cinzel:wght@400;500&family=EB+Garamond:wght@400&family=Kaushan+Script&family=Marcellus&display=swap">
<style>
  :root {
    --backdrop: #7e517d;
    --label-paper: #ffffff;
    --ink: #111111;
    --rose-light: #f6c9dc;
    --rose: #ee9ebf;
    --rose-deep: #e47fa9;
    --band-text: #ffffff;
    --fine-text: #2a2a2a;
  }
  * { margin: 0; padding: 0; box-sizing: border-box; }
  html, body {
    width: 1200px; height: 1200px; overflow: hidden;
    background: var(--backdrop);
  }
  .canvas {
    position: relative; width: 1200px; height: 1200px;
  }
  .label-shape {
    position: absolute; inset: 0;
  }
  .label-shape polygon { fill: var(--label-paper); }

  .brand-mark {
    position: absolute; left: 565px; top: 250px;
    width: 70px; height: 70px; background: var(--ink);
  }
  .brand-name {
    position: absolute; left: 0; width: 1200px; text-align: center;
    font-family: "Marcellus", serif; color: var(--ink); font-weight: 400;
  }
  .brand-name--main { top: 470px; font-size: 34px; letter-spacing: 1px; }
  .brand-name--sub  { top: 512px; font-size: 17px; letter-spacing: 7px; }

  .product-title {
    position: absolute; left: 0; width: 1200px; top: 640px; text-align: center;
    font-family: "Cinzel", serif; font-weight: 400; font-size: 104px; line-height: 1;
    letter-spacing: 2px;
    background: linear-gradient(100deg, var(--rose-light), var(--rose) 40%, var(--rose-light) 60%, var(--rose-deep));
    -webkit-background-clip: text; background-clip: text; color: transparent;
  }
  .product-grade {
    position: absolute; left: 0; width: 1200px; top: 712px; text-align: center;
    font-family: "Kaushan Script", cursive; font-size: 64px; line-height: 1;
    color: var(--ink); transform: rotate(-3deg);
  }

  .filter-band {
    position: absolute; left: 270px; top: 868px; width: 654px; height: 48px;
    background: linear-gradient(90deg, var(--rose-deep), var(--rose) 50%, var(--rose-light) 70%, var(--rose-deep));
    display: flex; align-items: center; justify-content: center;
    font-family: "Cinzel", serif; font-weight: 500; font-size: 30px;
    letter-spacing: 6px; color: var(--band-text);
  }
  .origin {
    position: absolute; left: 0; width: 1200px; top: 932px; text-align: center;
    font-family: "EB Garamond", serif; font-size: 23px; color: var(--fine-text);
  }
  .volume {
    position: absolute; left: 0; width: 1200px; top: 1012px; text-align: center;
    font-family: "EB Garamond", serif; font-size: 23px; line-height: 33px;
    color: var(--fine-text);
  }
</style>
</head>
<body>
  <main class="canvas">
    <svg class="label-shape" width="1200" height="1200" viewBox="0 0 1200 1200" aria-hidden="true">
      <polygon points="600,60 948,934 655,1134 545,1134 252,934"/>
    </svg>

    <div class="brand-mark" aria-hidden="true"></div>
    <p class="brand-name brand-name--main">SILVER WREN</p>
    <p class="brand-name brand-name--sub">DISTILLERY</p>

    <h1 class="product-title">VODKA</h1>
    <p class="product-grade">Premium</p>

    <div class="filter-band">ROSE QUARTS FILTERED</div>
    <p class="origin">Handcrafted in Melbourne, Australia</p>
    <p class="volume">700ml VOL<br>40% ALC</p>
  </main>
</body>
</html>
```